Holbrook Legal Group
Project: Stationary for law firm
Stationary for law firm - Law
Stationary for law firm
Use standard fonts
TOMAS VERDELL
Principal Attorney
48210 Pellman Avenue, Suite 415 Woodland Hills, California 90812
legaldesk@brivomail.example
HolbrookLegalGroup.example
dmitrivlaw dmitrivlaw
Kindly note this logo is our old logo design. We have a new logo and files were uploaded.
Please see brief and uploaded files.

```html
<!DOCTYPE html>
<html lang="en">
<head>
<meta charset="utf-8">
<title>Holbrook Legal Group — Business Card</title>
<link href="https://fonts.googleapis.com/css2?family=Cinzel:wght@500&family=Michroma&family=Exo+2:wght@400;500&display=swap" rel="stylesheet">
<style>
  :root {
    --backdrop: #d6d7d9;
    --card: #ffffff;
    --slate: #56647d;
    --icon-grey: #7b7f86;
    --icon-light: #c9ccd2;
    --ink: #2f3a4d;
    --ink-soft: #4c5566;
    --on-slate: #eef1f6;
  }
  * { margin: 0; padding: 0; box-sizing: border-box; }
  html, body { width: 1200px; height: 948px; overflow: hidden; }
  body {
    background: var(--backdrop);
    font-family: "Exo 2", "Segoe UI", sans-serif;
    position: relative;
  }
  .card {
    position: absolute;
    width: 640px;
    height: 370px;
    background: var(--card);
    border-radius: 22px;
    overflow: hidden;
    box-shadow: 0 6px 18px rgba(0,0,0,0.12);
  }
  .card--front { left: 250px; top: 60px; }
  .card--back { left: 310px; top: 500px; }

  /* Front */
  .brand {
    position: absolute; left: 0; right: 0; top: 150px;
    text-align: center; color: var(--slate);
  }
  .brand__name {
    font-family: "Cinzel", Georgia, serif;
    font-weight: 500; font-size: 26px; letter-spacing: 1px;
  }
  .brand__tagline {
    margin-top: 6px;
    font-family: "Exo 2", sans-serif;
    font-size: 9px; letter-spacing: 3px; color: var(--ink-soft);
  }

  /* Back */
  .band {
    position: absolute; left: 0; right: 0; top: 150px; height: 190px;
    background: var(--slate);
  }
  .icon { position: absolute; }
  .person { position: absolute; left: 36px; top: 84px; color: var(--ink); }
  .person__name {
    font-family: "Michroma", sans-serif; font-size: 14px; letter-spacing: .5px;
  }
  .person__title { font-size: 11px; margin-top: 4px; color: var(--ink-soft); }
  .address {
    position: absolute; left: 212px; top: 82px; width: 220px;
    text-align: center; font-family: "Michroma", sans-serif;
    font-size: 9.5px; line-height: 17px; color: var(--ink);
  }
  .phones {
    position: absolute; right: 36px; top: 84px; text-align: right;
    font-family: "Michroma", sans-serif; font-size: 11px; line-height: 20px;
    color: var(--ink);
  }
  .web {
    position: absolute; left: 40px; top: 226px;
    font-size: 13px; line-height: 24px; color: var(--on-slate); letter-spacing: .3px;
  }
  .social { position: absolute; left: 370px; top: 172px; list-style: none; }
  .social__item {
    display: flex; align-items: center; gap: 12px; height: 40px;
    font-size: 12.5px; color: var(--on-slate); letter-spacing: .3px;
    white-space: nowrap;
  }
  .social__dot {
    width: 28px; height: 28px; border-radius: 50%; background: var(--icon-light);
    flex: none;
  }
</style>
</head>
<body>

<section class="card card--front" aria-label="Card front">
  <div class="brand">
    <div class="brand__name">Holbrook Legal Group</div>
    <div class="brand__tagline">ATTORNEYS AT LAW</div>
  </div>
</section>

<section class="card card--back" aria-label="Card back">
  <div class="band"></div>

  <svg class="icon" style="left:60px;top:28px" width="36" height="36" viewBox="0 0 36 36" aria-hidden="true">
    <circle cx="18" cy="18" r="18" fill="var(--icon-grey)"/>
    <circle cx="18" cy="14" r="5" fill="#fff"/>
    <path d="M9 27c1-5 5-7 9-7s8 2 9 7z" fill="#fff"/>
  </svg>
  <svg class="icon" style="left:304px;top:28px" width="36" height="36" viewBox="0 0 36 36" aria-hidden="true">
    <circle cx="18" cy="18" r="18" fill="var(--icon-grey)"/>
    <path d="M18 8a7 7 0 0 0-7 7c0 5 7 13 7 13s7-8 7-13a7 7 0 0 0-7-7z" fill="#fff"/>
    <circle cx="18" cy="15" r="2.6" fill="var(--icon-grey)"/>
  </svg>
  <svg class="icon" style="left:544px;top:28px" width="36" height="36" viewBox="0 0 36 36" aria-hidden="true">
    <circle cx="18" cy="18" r="18" fill="var(--icon-grey)"/>
    <rect x="12" y="8" width="12" height="20" rx="2" fill="#fff"/>
    <rect x="14" y="11" width="8" height="12" fill="var(--icon-grey)"/>
  </svg>

  <div class="person">
    <div class="person__name">TOMAS VERDELL</div>
    <div class="person__title">Principal Attorney</div>
  </div>
  <div class="address">48210 Pellman Avenue,<br>Suite 415, Woodland Hills<br>California 90812</div>
  <div class="phones">(818) 555-0142<br>(818) 555-0143</div>

  <svg class="icon" style="left:40px;top:172px" width="40" height="40" viewBox="0 0 40 40" aria-hidden="true">
    <circle cx="20" cy="20" r="20" fill="var(--icon-light)"/>
    <rect x="10" y="12" width="20" height="13" rx="1.5" fill="none" stroke="var(--slate)" stroke-width="2.2"/>
    <rect x="17" y="26" width="6" height="3" fill="var(--slate)"/>
  </svg>
  <div class="web">legaldesk@brivomail.example<br>HolbrookLegalGroup.example</div>

  <ul class="social">
    <li class="social__item"><span class="social__dot"></span>socialpage.example/dmitrivlaw</li>
    <li class="social__item"><span class="social__dot"></span>shortpost.example/dmitrivlaw</li>
    <li class="social__item"><span class="social__dot"></span>worknet.example/in/dmitrivlaw</li>
  </ul>
</section>

</body>
</html>
```